Guaranteed Web Design (Uncoded - PSD layout only) for kids psychologists, minor logo with runner up

Simple psychologist website
Open brief, creative designs encouraged
Site map:
Home
our services
our psychologists
selective mutism
resources
contact

Current website:
http://mindnest4tots.com.au/
Not in love with our logo, or colours etc - open brief
Happy for new font/style/logo for company name - if we choose a logo design from a designer who doesn't win the competition, we will award $50 for the logo and use it in the new website

Website made a few years ago for a sister company that we really like:
http://www.corlewpsychology.com.au/

Clean, credible and warm and friendly look & feel
stock photos OK, designer will be required to hand over any images used in the design as shown in the PSD

Target Market(s)

Adolescents with psychological issues and their families

Industry/Entity Type

Psychology

Number of Pages Required

2 page

Colors

Designer to choose colors to be used in the design.

Requirements
Must have
• One home page - simple with 2 or 3 small areas to tease and attract the user and one template page to suit all the other pages
• We like slides, we want to have 3 slides like corlewpsychology.com.au
• Three slide titles:
• 1. We specialise in many areas, find the right clinical psychologist for your family
• 2. Child Clinical Psychologists in Chatswood and Westmead
• 3. Resources
• Pages structurally similar to
• http://www.corlewpsychology.com.au/
• We like the 'featured' items, which in our case will have splash box titles (can be 3 or 4):
• 1. Selective Mutism
• 2. Is my child anxious?
• 3. Does my child have an eating disorder?
• 4. Parenting adolescents
• Does not need to be a copy of http://www.corlewpsychology.com.au/ and we are willing to accept outside-the-box thinking and design (we in fact encourage it)
• Owner of business wants to highlight Selective Mutism as they have specialists. Consider ways that may make this work.
• Design winner will be based on home page design but winning designer will be required to provide an additional but simpler 'standard' page template design based on the themes used in the winning design.

```html
<!DOCTYPE html>
<html lang="en">
<head>
<meta charset="utf-8">
<title>MindNest – Child, Adolescent &amp; Family Psychology</title>
<link href="https://fonts.googleapis.com/css2?family=Nunito+Sans:wght@400;600;700&family=Roboto:wght@400;500&display=swap" rel="stylesheet">
<style>
:root{
  --teal:#5fc8b5;
  --teal-dark:#3fb09c;
  --grey:#8a8a8e;
  --text:#333;
  --muted:#777;
  --footer:#1e1e1e;
  --white:#fff;
}
*{margin:0;padding:0;box-sizing:border-box}
html,body{width:745px;height:1200px;overflow:hidden;background:var(--white)}
body{position:relative;font-family:"Nunito Sans",Arial,sans-serif;color:var(--text)}
.abs{position:absolute}

/* header */
.brand{left:100px;top:16px;display:flex;align-items:center;gap:8px}
.brand-dot{width:40px;height:40px;border-radius:50%;background:var(--teal)}
.brand-name{font-family:"Roboto",sans-serif;font-weight:500;font-size:19px;color:var(--teal);letter-spacing:.5px;line-height:1}
.brand-tag{font-size:7px;color:var(--muted);margin-top:3px}
.topline{right:102px;top:13px;font-size:8px;color:var(--muted);display:flex;align-items:center;gap:8px}
.topline .call{color:var(--text);font-weight:600}
.main-nav{right:100px;top:43px;display:flex;gap:16px;font-size:8.5px;font-weight:600;color:#555}
.main-nav .active{color:var(--teal)}

/* hero */
.hero{left:0;top:66px;width:745px;height:400px;background:radial-gradient(circle at 78% 8%,#fff7d8 0,#f3c25e 12%,#8a6a2a 35%,#3b3317 62%,#1f2412 100%)}
.hero-title{left:101px;top:200px;font-size:16px;font-weight:600;color:var(--white);line-height:23px}
.hero-more{left:527px;top:314px;font-size:15px;font-weight:700;color:#111}
.dots{left:101px;top:410px;display:flex;gap:6px}
.dots span{width:9px;height:9px;border-radius:50%;background:var(--white)}
.dots .on{background:var(--teal);border:1.5px solid var(--white)}
.wave{left:0;top:360px}

/* welcome */
.welcome{left:0;top:496px;width:745px;text-align:center}
.welcome h1{font-family:"Roboto",sans-serif;font-weight:500;font-size:20px;color:var(--teal);letter-spacing:.3px}
.welcome .sub{font-size:7.5px;color:var(--muted);margin-top:1px}
.welcome h2{font-family:Arial,sans-serif;font-weight:400;font-size:9.5px;color:#222;margin-top:14px}
.welcome p{font-family:Arial,sans-serif;font-size:7.8px;line-height:13px;color:#333;width:550px;margin:8px auto 0}
.welcome a{display:inline-block;margin-top:11px;font-size:7.5px;color:var(--teal);text-decoration:underline}

/* featured */
.feature-band{left:0;top:700px;width:745px;height:156px;background:var(--teal)}
.feature{top:655px;width:130px;text-align:center;color:var(--white)}
.feature .frame{background:var(--white);padding:3px;height:80px}
.feature .photo{height:74px}
.feature h3{font-size:9.5px;font-weight:600;color:#263a36;margin-top:11px;line-height:12px}
.feature p{font-family:Arial,sans-serif;font-size:7px;line-height:10.5px;margin-top:8px;padding:0 6px}
.feature .plus{display:block;margin:7px auto 0}

/* map & contact */
.map{left:0;top:856px;width:745px;height:246px;background:linear-gradient(135deg,#eceae4,#e2e4de 55%,#d8e8cf)}
.contact{left:384px;top:908px;width:252px;height:140px;background:rgba(255,255,255,.86);padding:10px 12px}
.contact h3{font-family:"Roboto",sans-serif;font-weight:500;font-size:14px;color:var(--grey)}
.contact h3 b{color:var(--teal);font-weight:500}
.tabs{display:flex;gap:7px;font-size:6.8px;margin:6px 0 0 24px;border-bottom:1px solid #ddd;width:160px;padding-bottom:2px}
.tabs .on{color:var(--teal)}
.row{display:flex;gap:8px;font-size:6.6px;line-height:10px;margin-top:9px}
.row svg{flex:none}
.directions{font-size:6.8px;color:var(--teal);text-decoration:underline;margin:4px 0 0 20px;display:block}

/* footer */
.footer{left:0;top:1102px;width:745px;height:98px;background:var(--footer);color:var(--white)}
.foot-nav{left:100px;top:20px;display:flex;gap:15px;font-size:8px}
.foot-nav .active{color:var(--teal)}
.follow{left:100px;top:44px;display:flex;align-items:center;gap:7px;font-size:8px}
.follow span.c{width:19px;height:19px;border-radius:50%;border:1.5px solid var(--white);background:#3b5aa8}
.follow span.c.tw{background:#2aa6de}
.follow span.c.yt{background:#d8322a}
.copy{left:100px;top:75px;font-size:7.5px}
.foot-brand{left:535px;top:10px;text-align:center;width:108px}
.foot-brand .dot{width:36px;height:36px;border-radius:50%;background:var(--teal);margin:0 auto 6px}
.foot-brand .name{font-family:"Roboto",sans-serif;font-weight:500;font-size:16px;color:var(--teal);letter-spacing:.5px}
.foot-brand .tag{font-size:6.3px;color:#999}
</style>
</head>
<body>

<header>
  <div class="abs brand">
    <span class="brand-dot"></span>
    <div>
      <div class="brand-name">MINDNEST</div>
      <div class="brand-tag">Child, Adolescent &amp; Family Psychology</div>
    </div>
  </div>
  <div class="abs topline">
    <span>For Chatswood And Westmead Offices</span>
    <svg width="13" height="13" viewBox="0 0 13 13"><circle cx="6.5" cy="6.5" r="6" fill="none" stroke="#5fc8b5"/><path d="M4.5 3.5c-.8 1.8.5 4.5 3 5.8l.9-.9" fill="none" stroke="#5fc8b5" stroke-width="1.1"/></svg>
    <span class="call">Call us on 0400 527 318</span>
  </div>
  <nav class="abs main-nav">
    <span class="active">Home</span><span>Our Services</span><span>Our Psychologists</span><span>Selective Mustim</span><span>Resources</span><span>Contact Us</span>
  </nav>
</header>

<section>
  <div class="abs hero" role="img" aria-label="Sunlit meadow with a clover flower in the grass at sunset"></div>
  <div class="abs hero-title">Child Clinical<br>Psychology Resources</div>
  <div class="abs hero-more">More...</div>
  <div class="abs dots"><span></span><span class="on"></span><span></span></div>
  <svg class="abs wave" width="745" height="115" viewBox="0 0 745 115">
    <path d="M0 10 C60 110 180 110 330 80 C470 50 620 0 745 15 L745 115 L0 115Z" fill="#fff"/>
    <path d="M0 10 C40 70 120 100 220 98 C140 100 60 80 0 45Z" fill="#8a8a8e"/>
    <path d="M0 25 C70 105 200 110 330 82 C470 52 620 5 745 15 L745 26 C620 18 470 62 330 92 C200 118 60 100 0 40Z" fill="#5fc8b5"/>
    <path d="M465 63 C560 35 660 30 745 35 L745 55 C660 45 560 48 465 63Z" fill="#8a8a8e"/>
  </svg>
</section>

<section class="abs welcome">
  <h1>WELCOME TO MINDNEST</h1>
  <div class="sub">Child, Adolescent &amp; Family Psychology</div>
  <h2>We Provide Expert Treatment If Depression, Anxiety &amp; Eating Disorders</h2>
  <p>We are a group of clinical psychologists at Chatswood and Westmead (Sydney). We provide a range of services including the following: Individual counselling and therapy for kids, teens and families, Family Consultations, Seminars and training with schools, Brief group programmes for anxiety, stress and body image concerns for adolescents.</p>
  <a>Read More</a>
</section>

<div class="abs feature-band"></div>
<article class="abs feature" style="left:100px">
  <div class="frame"><div class="photo" role="img" aria-label="Young boy holding a small handwritten greeting card" style="background:linear-gradient(160deg,#c98a5a,#8a4d2e 60%,#4b2b1e)"></div></div>
  <h3>Selective<br>Mutism</h3>
  <p>Sed ut perspiciatis unde omnis iste natus error sit voluptatem accu santium doloremque.</p>
  <svg class="plus" width="14" height="14" viewBox="0 0 14 14"><rect x=".5" y=".5" width="13" height="13" fill="none" stroke="#fff"/><path d="M7 4v6M4 7h6" stroke="#fff"/></svg>
</article>
<article class="abs feature" style="left:238px">
  <div class="frame"><div class="photo" role="img" aria-label="Sad girl sitting alone hugging her knees" style="background:linear-gradient(160deg,#b8a890,#7a6a58 55%,#4e4438)"></div></div>
  <h3>Is My Child<br>Anxious?</h3>
  <p>Sed ut perspiciatis unde omnis iste natus error sit voluptatem accu santium doloremque.</p>
  <svg class="plus" width="14" height="14" viewBox="0 0 14 14"><rect x=".5" y=".5" width="13" height="13" fill="none" stroke="#fff"/><path d="M7 4v6M4 7h6" stroke="#fff"/></svg>
</article>
<article class="abs feature" style="left:376px">
  <div class="frame"><div class="photo" role="img" aria-label="Boy sitting at a table looking at a plate of food" style="background:linear-gradient(160deg,#f2efe9,#d9d4cb 55%,#a99a86)"></div></div>
  <h3>Does My Child Have An<br>Eating Disorder?</h3>
  <p>Sed ut perspiciatis unde omnis iste natus error sit voluptatem accu santium doloremque.</p>
  <svg class="plus" width="14" height="14" viewBox="0 0 14 14"><rect x=".5" y=".5" width="13" height="13" fill="none" stroke="#fff"/><path d="M7 4v6M4 7h6" stroke="#fff"/></svg>
</article>
<article class="abs feature" style="left:514px">
  <div class="frame"><div class="photo" role="img" aria-label="Parents with a child talking to a counsellor" style="background:linear-gradient(160deg,#e8e2d8,#9fb0c4 55%,#5a6f8a)"></div></div>
  <h3>Parenting<br>Adolescents</h3>
  <p>Sed ut perspiciatis unde omnis iste natus error sit voluptatem accu santium doloremque.</p>
  <svg class="plus" width="14" height="14" viewBox="0 0 14 14"><rect x=".5" y=".5" width="13" height="13" fill="none" stroke="#fff"/><path d="M7 4v6M4 7h6" stroke="#fff"/></svg>
</article>

<section>
  <div class="abs map" role="img" aria-label="Street map of Westmead and Parramatta showing the clinic location"></div>
  <div class="abs contact">
    <h3><b>Contact</b> Details</h3>
    <div class="tabs"><span class="on">Westmead</span><span>Chatswood</span></div>
    <div class="row">
      <svg width="9" height="10" viewBox="0 0 9 10"><path d="M4.5 0a3.5 3.5 0 0 0-3.5 3.5C1 6 4.5 10 4.5 10S8 6 8 3.5A3.5 3.5 0 0 0 4.5 0z" fill="#5fc8b5"/><circle cx="4.5" cy="3.5" r="1.3" fill="#fff"/></svg>
      <span style="margin-top:7px">Suite 204, level 2, The Harbourview Clinic<br>88 Larkspur Road, Westmead NSW 2145<br><span style="display:block;margin-top:5px">0400 527 318 (P) , (02) 9740 3185 (F)</span></span>
    </div>
    <div class="row">
      <svg width="9" height="8" viewBox="0 0 9 8"><rect width="9" height="7" y=".5" fill="#5fc8b5"/><path d="M0 .5l4.5 3.5L9 .5" fill="none" stroke="#fff" stroke-width=".8"/></svg>
      <span>info@mindnest4tots.com.au</span>
    </div>
    <a class="directions">Get Directions Here</a>
  </div>
</section>

<footer class="abs footer">
  <nav class="abs foot-nav"><span class="active">Home</span><span>Our Services</span><span>Our Psychologists</span><span>Selective Mustim</span><span>Resources</span><span>Contact Us</span></nav>
  <div class="abs follow"><span>Follow Us On</span><span class="c"></span><span class="c tw"></span><span class="c yt"></span></div>
  <div class="abs copy">Copyright © 2017 Brightwater Centre. All Rights Reserved.</div>
  <div class="abs foot-brand">
    <div class="dot"></div>
    <div class="name">MINDNEST</div>
    <div class="tag">Child, Adolescent &amp; Family Psychology</div>
  </div>
</footer>

</body>
</html>
```